New Company Business Card design

Looking for a corporate looking business card utilising my new logo design - the logo i would like embossed as one option and flat as another - simplistic but stylish - less is more - we are an import export business launching into the market - i would like a couple of options as main background - Grey or Black

```html
<!DOCTYPE html>
<html lang="en">
<head>
<meta charset="utf-8">
<title>Meridian Trade Partners – Business Card</title>
<link rel="stylesheet" href="https://fonts.googleapis.com/css2?family=Work+Sans:wght@400;500;600&display=swap">
<style>
  :root {
    --backdrop: #262626;
    --card: #1b1b1c;
    --card-edge: #2c2c2d;
    --brand-blue: #1a78c8;
    --ink-light: #f2f2f2;
    --ink-muted: #c9c9c9;
  }
  * { box-sizing: border-box; margin: 0; padding: 0; }
  html, body {
    width: 1200px; height: 900px; overflow: hidden;
    background: var(--backdrop);
    font-family: "Work Sans", Arial, sans-serif;
  }
  .canvas { position: relative; width: 1200px; height: 900px; }
  .card {
    position: absolute;
    width: 700px; height: 400px;
    background: linear-gradient(135deg, var(--card) 0%, var(--card-edge) 100%);
    box-shadow: 0 18px 40px rgba(0,0,0,0.55);
  }
  .card--front { left: 330px; top: 40px; }
  .card--back { left: 150px; top: 470px; }

  .brand {
    display: flex; align-items: center; gap: 12px;
    color: var(--brand-blue);
    font-weight: 600; letter-spacing: 0.06em; text-transform: uppercase;
    white-space: nowrap;
  }
  .brand__dot {
    width: 16px; height: 16px; border-radius: 50%;
    background: var(--brand-blue);
  }
  .tagline {
    color: var(--ink-light);
    font-weight: 400; text-transform: uppercase; letter-spacing: 0.32em;
    white-space: nowrap;
  }

  .card--front .lockup {
    position: absolute; left: 0; right: 0; top: 150px;
    display: flex; flex-direction: column; align-items: center; gap: 14px;
  }
  .card--front .brand { font-size: 28px; }
  .card--front .tagline { font-size: 11px; }

  .card--back .glow {
    position: absolute; left: 0; top: 0; width: 330px; height: 400px;
    background: radial-gradient(ellipse at 35% 55%, rgba(255,255,255,0.08) 0%, rgba(255,255,255,0) 70%);
  }
  .card--back .details {
    position: absolute; right: 44px; top: 60px;
    display: flex; flex-direction: column; align-items: flex-end;
    text-align: right;
  }
  .card--back .brand { font-size: 19px; gap: 9px; }
  .card--back .brand__dot { width: 12px; height: 12px; }
  .card--back .tagline { font-size: 8px; margin-top: 8px; letter-spacing: 0.28em; }
  .person__name {
    margin-top: 36px;
    color: var(--brand-blue); font-size: 26px; font-weight: 500; letter-spacing: 0.02em;
    text-transform: uppercase;
  }
  .person__role { color: var(--ink-light); font-size: 17px; margin-top: 4px; }
  .address { color: var(--ink-light); font-size: 17px; line-height: 1.35; margin-top: 12px; }
  .contact { list-style: none; margin-top: 12px; }
  .contact li {
    display: flex; align-items: center; justify-content: flex-end; gap: 12px;
    color: var(--ink-light); font-size: 17px; line-height: 1.45;
  }
  .contact .accent { color: var(--brand-blue); }
  .contact svg { width: 13px; height: 13px; flex: none; }
</style>
</head>
<body>
<main class="canvas">

  <section class="card card--front" aria-label="Card front">
    <div class="lockup">
      <div class="brand"><span class="brand__dot"></span>Meridian Trade Partners</div>
      <p class="tagline">Worldwide supply for every market</p>
    </div>
  </section>

  <section class="card card--back" aria-label="Card back">
    <div class="glow" role="img" aria-label="Large embossed brand decoration area"></div>
    <div class="details">
      <div class="brand"><span class="brand__dot"></span>Meridian Trade Partners</div>
      <p class="tagline">Worldwide supply for every market</p>
      <h1 class="person__name">Daniel Hart</h1>
      <p class="person__role">Director</p>
      <p class="address">2250 Harbor View Ave<br>Oakdale, CA 95361-2040</p>
      <ul class="contact">
        <li>555-204-7731
          <svg viewBox="0 0 24 24" fill="none" stroke="var(--brand-blue)" stroke-width="2"><path d="M5 3h4l2 5-2.5 1.5a11 11 0 0 0 6 6L16 13l5 2v4a2 2 0 0 1-2 2A16 16 0 0 1 3 5a2 2 0 0 1 2-2z"/></svg>
        </li>
        <li>hello@meridiantrade.com
          <svg viewBox="0 0 24 24" fill="none" stroke="var(--brand-blue)" stroke-width="2"><rect x="3" y="5" width="18" height="14" rx="1"/><path d="M3 6l9 7 9-7"/></svg>
        </li>
        <li><span>www.<span class="accent">meridiantrade</span>.com</span>
          <svg viewBox="0 0 24 24" fill="none" stroke="var(--brand-blue)" stroke-width="2"><circle cx="12" cy="12" r="9"/><path d="M3 12h18M12 3c3 3 3 15 0 18M12 3c-3 3-3 15 0 18"/></svg>
        </li>
      </ul>
    </div>
  </section>

</main>
</body>
</html>
```